Leading In-Home Tutoring Company Needs Web Banners

We need a suite of web banners for our re-marketing campaign. We are based in Melbourne and heading into the busiest time of the year with back to school and we would like to help guide parents to working with us via quality designed banners with the right CTAs. Banner specs as follows (W x H in pixels)
Medium Rectangle: 300 x 250
Vertical rectangle: 240 x 400
Banner: 468 x 60
Leaderboard: 728 x 90
Square: 250 x 250
Mobile leaderboard: 320 x 50
Updates

Hi designers I'm new to this and didn't realise that I had to upload all files at the beginning. I have images that can be used for this project. Just need to work out how to upload them. Added Sunday, January 22, 2017

Hi awesome designers... I've updated the brief now with new files :)

Target Market(s)

Mothers who value kids education. Our customer can be found having morning coffee with friends in her lycra as she prepares to go to the gym. Middle class, inner city and suburban Mums. Most likely on Friendnook.

Industry/Entity Type

It Company

Font styles to use
Sans Serif

Colors
0692cd
fbed22
f47f39
ec1f27

Requirements
Must have
• Wording should include.
• What we do: 1:1, In-Home Tutoring
• Value proposition: The Best Tutor For Your Child
• Call to Action - Free Assessment > Find Out More
• Adjusted layout to suit the sizes. Use of image where possible to provide immediate graphic display of what we do
Nice to have
• Keep it simple, create an emotive connection. Kids matter to parents and they will pay for services if we can create banners that show we care and can help wtih their education.
Should not have
• Anything negative or use fear marketing

```html
<!DOCTYPE html>
<html lang="en">
<head>
<meta charset="utf-8">
<title>LearnLumen Web Banner Suite</title>
<link href="https://fonts.googleapis.com/css2?family=Roboto:wght@400;500;700&display=swap" rel="stylesheet">
<style>
:root{
  --stage:#4b4c4e;
  --orange:#f47f39;
  --blue:#0692cd;
  --red:#ec1f27;
  --logo-blue:#2d72a8;
  --white:#ffffff;
  --ink:#1d1d1d;
  --photo-warm:linear-gradient(135deg,#8a6d5a 0%,#c9b6a4 45%,#5b6f92 100%);
  --photo-brick:linear-gradient(135deg,#8e4a38 0%,#a8634d 40%,#2f3f3a 100%);
  --photo-study:linear-gradient(135deg,#7d6a63 0%,#b8a69c 50%,#4a3e46 100%);
}
*{box-sizing:border-box;margin:0;padding:0}
html,body{width:1200px;height:960px;overflow:hidden}
body{background:var(--stage);font-family:"Roboto",Arial,sans-serif;position:relative}
.banner{position:absolute;background:var(--white);overflow:hidden}
.photo{position:absolute;left:0;top:0}
.shapes{position:absolute;left:0;top:0}
.headline{position:absolute;color:var(--white);font-weight:700;text-align:center;line-height:1.12;text-shadow:1px 2px 2px rgba(0,0,0,.55);transform:translateX(-50%);white-space:nowrap}
.offer{position:absolute;color:var(--ink);font-weight:500;text-align:center;transform:translateX(-50%);white-space:nowrap}
.cta{position:absolute;transform:translateX(-50%);background:var(--red);color:var(--white);font-weight:500;text-transform:uppercase;border-radius:999px;border:2px solid var(--white);box-shadow:1px 2px 3px rgba(0,0,0,.35);display:flex;align-items:center;justify-content:center;white-space:nowrap}
.brand{position:absolute;display:flex;align-items:center;gap:.35em;color:var(--logo-blue);font-weight:500;white-space:nowrap}
.brand-dot{width:.45em;height:.45em;border-radius:50%;background:var(--orange)}
.size-label{position:absolute;color:var(--white);font-weight:700;font-size:20px;letter-spacing:.5px}
</style>
</head>
<body>

<!-- Medium rectangle 300 x 250 -->
<section class="banner medium-rectangle" style="left:81px;top:56px;width:360px;height:300px">
  <div class="photo" role="img" aria-label="Tutor helping a schoolboy with his work at a desk in front of a bookshelf" style="width:360px;height:209px;background:var(--photo-study)"></div>
  <svg class="shapes" width="360" height="212" viewBox="0 0 360 212">
    <polygon points="147,0 178,0 262,209 238,209" fill="var(--blue)"/>
    <polygon points="176,0 360,0 360,209 260,209" fill="var(--orange)"/>
    <rect x="0" y="209" width="360" height="2" fill="var(--blue)"/>
  </svg>
  <div class="headline" style="left:286px;top:44px;font-size:27px">1:1,<br>In-Home<br>Tutoring</div>
  <div class="brand" style="left:38px;top:250px;font-size:21px"><span class="brand-dot"></span>LearnLumen</div>
  <div class="offer" style="left:271px;top:231px;font-size:12px">Free Assessment</div>
  <div class="cta" style="left:271px;top:248px;width:124px;height:26px;font-size:12.5px">Find Out More</div>
</section>
<div class="size-label" style="left:331px;top:400px">300 X 250</div>

<!-- Vertical rectangle 240 x 400 -->
<section class="banner vertical-rectangle" style="left:514px;top:56px;width:287px;height:481px">
  <div class="photo" role="img" aria-label="Parent sitting beside a child who is writing at a table" style="width:287px;height:313px;background:var(--photo-warm)"></div>
  <svg class="shapes" width="287" height="315" viewBox="0 0 287 315">
    <polygon points="102,0 128,0 284,313 272,313" fill="var(--blue)"/>
    <polygon points="127,0 287,0 287,313 283,313" fill="var(--orange)"/>
    <rect x="0" y="312" width="287" height="2" fill="var(--orange)"/>
  </svg>
  <div class="headline" style="left:222px;top:26px;font-size:23px">The Best<br>Tutor<br>for Your<br>Child</div>
  <div class="brand" style="left:143px;top:357px;font-size:25px;transform:translateX(-50%)"><span class="brand-dot"></span>LearnLumen</div>
  <div class="offer" style="left:147px;top:411px;font-size:12.5px">Free Assessment</div>
  <div class="cta" style="left:146px;top:427px;width:134px;height:28px;font-size:13px">Find Out More</div>
</section>
<div class="size-label" style="left:688px;top:544px">240 X 400</div>

<!-- Square 250 x 250 -->
<section class="banner square" style="left:821px;top:231px;width:300px;height:300px">
  <div class="photo" role="img" aria-label="Group of smiling school children in uniform standing against a brick wall" style="width:300px;height:209px;background:var(--photo-brick)"></div>
  <svg class="shapes" width="300" height="209" viewBox="0 0 300 209">
    <polygon points="102,0 131,0 203,209 190,209" fill="var(--blue)"/>
    <polygon points="130,0 300,0 300,209 201,209" fill="var(--orange)"/>
  </svg>
  <div class="headline" style="left:232px;top:30px;font-size:23px">The Best<br>Tutor<br>for Your<br>Child</div>
  <div class="brand" style="left:20px;top:252px;font-size:20px"><span class="brand-dot"></span>LearnLumen</div>
  <div class="offer" style="left:221px;top:227px;font-size:12px">Free Assessment</div>
  <div class="cta" style="left:217px;top:242px;width:120px;height:26px;font-size:12.5px">Find Out More</div>
</section>
<div class="size-label" style="left:1006px;top:544px">250 X 250</div>

<!-- Mobile leaderboard 320 x 50 -->
<section class="banner mobile-leaderboard" style="left:73px;top:473px;width:384px;height:59px">
  <div class="photo" role="img" aria-label="School children in uniform standing in a row against a brick wall" style="width:122px;height:59px;background:var(--photo-brick)"></div>
  <svg class="shapes" width="211" height="59" viewBox="0 0 211 59">
    <polygon points="94,0 108,0 127,59 120,59" fill="var(--blue)"/>
    <polygon points="106,0 211,0 211,59 124,59" fill="var(--orange)"/>
  </svg>
  <div class="headline" style="left:167px;top:5px;font-size:12.5px;line-height:1.35">1:1,<br>In-Home<br>Tutoring</div>
  <div class="brand" style="left:222px;top:24px;font-size:10px"><span class="brand-dot"></span>LearnLumen</div>
  <div class="offer" style="left:339px;top:15px;font-size:7.5px">Free Assessment</div>
  <div class="cta" style="left:339px;top:24px;width:78px;height:15px;font-size:7px;border-width:1px">Find Out More</div>
</section>
<div class="size-label" style="left:338px;top:546px">320 X 50</div>

<!-- Banner 468 x 60 -->
<section class="banner full-banner" style="left:77px;top:606px;width:561px;height:71px">
  <div class="photo" role="img" aria-label="Tutor and schoolboy working together at a desk in front of a bookshelf" style="width:212px;height:71px;background:var(--photo-study)"></div>
  <svg class="shapes" width="348" height="71" viewBox="0 0 348 71">
    <polygon points="176,0 192,0 218,71 208,71" fill="var(--blue)"/>
    <polygon points="190,0 348,0 348,71 214,71" fill="var(--orange)"/>
  </svg>
  <div class="headline" style="left:284px;top:13px;font-size:15.5px;line-height:1.25">The Best Tutor<br>for Your Child</div>
  <div class="brand" style="left:356px;top:34px;font-size:14px"><span class="brand-dot"></span>LearnLumen</div>
  <div class="offer" style="left:507px;top:22px;font-size:8.5px">Free Assessment</div>
  <div class="cta" style="left:505px;top:32px;width:92px;height:19px;font-size:8.5px;border-width:1.5px">Find Out More</div>
</section>
<div class="size-label" style="left:646px;top:650px">468 X60</div>

<!-- Leaderboard 728 x 90 -->
<section class="banner leaderboard" style="left:77px;top:714px;width:882px;height:107px">
  <div class="photo" role="img" aria-label="Smiling tutor and teenage student sitting together in a bright study" style="width:348px;height:107px;background:var(--photo-warm)"></div>
  <svg class="shapes" width="674" height="107" viewBox="0 0 674 107">
    <polygon points="288,0 318,0 347,107 336,107" fill="var(--blue)"/>
    <polygon points="316,0 674,0 674,107 345,107" fill="var(--orange)"/>
  </svg>
  <div class="headline" style="left:512px;top:17px;font-size:21.5px">The Best Tutor for Your Child</div>
  <div class="offer" style="left:521px;top:55px;font-size:11.5px;color:#2a2a2a">Free Assessment</div>
  <div class="cta" style="left:516px;top:70px;width:152px;height:26px;font-size:13px">Find Out More</div>
  <div class="brand" style="left:770px;top:56px;font-size:25px;transform:translateX(-50%)"><span class="brand-dot"></span>LearnLumen</div>
</section>
<div class="size-label" style="left:850px;top:828px">728 X 90</div>

</body>
</html>
```